Moden - Mexicali - Flower Shop

brisapetals is looking for a cool web design that has a airy, clean, mexicali feel to it.

See attached images and links for idea of what we mean with the above.

please no templates.
Updates

Target Market(s)

Local flower shop in San Diego, California

Industry/Entity Type

Shop

Requirements
Must have
• see. brisapetals.quillcart.example - I did the site and logo...I love the logo - hate the site.

Going for this feel: http://www.plumnotebook.example/tablecraft/archives/verandos.php

I also attached another site I liked- I just feel like it may be to busy.

```html
<!DOCTYPE html>
<html lang="en">
<head>
<meta charset="utf-8">
<title>brisapetals – Flower Shop</title>
<link href="https://fonts.googleapis.com/css2?family=Questrial&family=Mulish:ital,wght@0,400;0,600;0,700;0,800;1,700;1,800&display=swap" rel="stylesheet">
<style>
:root{
  --page:#f6f4e9;
  --topbar:#fbfbf6;
  --white:#ffffff;
  --salmon:#f98a6b;
  --coral:#ea5f62;
  --green:#8dc462;
  --price:#e8505b;
  --text:#6f6f6f;
  --muted:#8d8d8d;
  --line:#e4e2da;
  --brown:#b06d1c;
  --logo:#7fbcc4;
}
*{margin:0;padding:0;box-sizing:border-box}
html,body{width:949px;height:1200px;overflow:hidden}
body{background:var(--page);font-family:"Questrial",sans-serif;color:var(--text);position:relative}
.abs{position:absolute}

.topbar{left:0;top:0;width:949px;height:41px;background:var(--topbar);box-shadow:0 1px 3px rgba(0,0,0,.12)}
.toplinks{left:92px;top:13px;font-size:13px;color:var(--muted);display:flex;gap:27px}
.cart{left:672px;top:13px;font-size:13px;color:var(--muted);display:flex;align-items:center;gap:6px}

.logo-box{left:92px;top:65px;width:359px;height:84px;background:var(--white);display:flex;align-items:center;justify-content:center;gap:16px}
.logo-mark{width:30px;height:30px;border-radius:50%;border:2px solid var(--logo)}
.logo-name{font-family:"Questrial",sans-serif;font-size:27px;letter-spacing:9px;color:var(--logo)}

.search{left:583px;top:91px;width:274px;height:33px;display:flex}
.search-field{flex:1;background:var(--white);border:1px solid #dcdcd4;font-size:12px;color:var(--muted);padding:9px 14px}
.search-btn{width:42px;background:var(--green);display:flex;align-items:center;justify-content:center}

.mainnav{left:92px;top:167px;width:764px;height:41px;background:var(--salmon);display:flex;font-family:"Mulish",sans-serif;font-weight:700;font-size:12.5px;color:var(--white)}
.mainnav span{display:flex;align-items:center;justify-content:center;border-right:1px solid rgba(255,255,255,.35)}
.mainnav .current{color:#ffd24a}

.hero{left:92px;top:225px;width:517px;height:247px;background:linear-gradient(120deg,#e4e1d2 0%,#f5f4ee 40%,#f1ede0 70%,#e2dcc0 100%)}
.hero-arrow{top:337px;width:40px;height:33px;background:rgba(222,110,80,.85);display:flex;align-items:center;justify-content:center}

.promo-wedding{left:636px;top:225px;width:221px;height:112px;background:linear-gradient(90deg,#e9c5cf 0%,#f7eef1 45%,#fdfbfc 100%);border:1px solid var(--line)}
.promo-wedding .label{position:absolute;right:16px;top:22px;font-size:18px;color:#ef7da6}
.promo-wedding .sub{position:absolute;right:26px;top:42px;font-size:7px;color:#888}
.promo-wedding .off{position:absolute;left:110px;top:40px;font-size:38px;color:#f29ab8}
.promo-wedding .more{position:absolute;right:20px;top:88px;font-family:"Mulish",sans-serif;font-style:italic;font-weight:700;font-size:11.5px;color:#ef7da6}

.promo-shipping{left:636px;top:359px;width:221px;height:111px;background:var(--green);color:var(--white)}
.promo-shipping .title{position:absolute;left:72px;top:33px;font-family:"Mulish",sans-serif;font-style:italic;font-weight:800;font-size:20px}
.promo-shipping .sub{position:absolute;left:73px;top:60px;font-size:12.5px}

.section-head{height:30px;color:var(--white);font-size:13.5px;padding:8px 12px}
.curated-head{left:92px;top:491px;width:517px;background:var(--coral)}
.curated-head .all{position:absolute;right:12px;top:9px;font-family:"Mulish",sans-serif;font-style:italic;font-size:10.5px}
.fresh-head{left:636px;top:491px;width:221px;background:var(--salmon);padding-left:14px}

.card{width:155px;height:213px;background:var(--white);border:1px solid var(--line);padding:3px}
.card .photo{width:147px;height:106px}
.card .name{font-size:12.5px;margin:14px 0 0 4px}
.price-row{display:flex;align-items:baseline;gap:9px;margin:6px 0 0 4px}
.price{font-family:"Mulish",sans-serif;font-weight:700;font-size:21px;color:var(--price)}
.was{font-family:"Mulish",sans-serif;font-style:italic;font-weight:700;font-size:11.5px;color:#777;text-decoration:line-through}
.add{display:inline-block;margin:8px 0 0 4px;background:var(--green);color:var(--white);font-size:9.5px;padding:7px 8px;width:78px;text-align:center}

.fresh-panel{left:636px;top:522px;width:221px;height:367px;background:var(--white)}
.fresh-item{position:absolute;left:14px;width:184px;height:72px;border-bottom:1px solid #ececec}
.fresh-item .thumb{position:absolute;left:0;top:0;width:54px;height:54px}
.fresh-item .name{position:absolute;left:70px;top:1px;font-size:12.5px;color:var(--muted)}
.fresh-item .prices{position:absolute;left:70px;top:19px;display:flex;gap:8px;align-items:baseline}
.fresh-item .now{font-family:"Mulish",sans-serif;font-style:italic;font-weight:700;font-size:15px;color:var(--salmon)}
.fresh-item .old{font-family:"Mulish",sans-serif;font-style:italic;font-weight:700;font-size:12px;color:#888}
.fresh-item .buy{position:absolute;left:73px;top:43px;font-family:"Mulish",sans-serif;font-weight:700;font-size:10.5px;color:var(--green)}

.footer{left:0;top:1031px;width:949px;height:131px;background:var(--white)}
.footer h3{font-family:"Mulish",sans-serif;font-weight:700;font-size:14px;color:var(--brown);margin-bottom:6px}
.footer p,.footer li{font-size:11px;line-height:15.5px;color:var(--muted);list-style:none}
.footer .dark{color:#333}
.social{display:flex;gap:9px;margin-top:10px}
.social span{width:14px;height:14px;background:#3d6c7a;border-radius:2px}
.newsletter{display:flex;gap:5px;margin-top:12px}
.newsletter .field{width:149px;height:29px;border:1px solid #ccc;border-radius:3px;font-size:11px;color:var(--muted);padding:7px 9px}
.newsletter .btn{width:59px;height:29px;background:var(--green);border-radius:3px;color:var(--white);font-size:11px;display:flex;align-items:center;justify-content:center}

.copyright{left:0;top:1162px;width:949px;height:38px;background:var(--coral);color:var(--white);font-size:10.5px;display:flex;align-items:center;justify-content:center}
</style>
</head>
<body>

<header class="abs topbar">
  <nav class="abs toplinks"><span>WishList(0)</span><span>Checkout</span><span>Login</span><span>CreateanAccount</span></nav>
  <div class="abs cart">
    <svg width="15" height="13" viewBox="0 0 15 13"><path d="M0 1h3l2 7h8l2-6H4" fill="none" stroke="#e8505b" stroke-width="1.6"/><circle cx="6" cy="11" r="1.4" fill="#e8505b"/><circle cx="12" cy="11" r="1.4" fill="#e8505b"/></svg>
    <span>My Cart: 0 item(s) - $0.00</span>
    <svg width="8" height="5" viewBox="0 0 8 5"><path d="M1 1l3 3 3-3" fill="none" stroke="#e8505b" stroke-width="1.4"/></svg>
  </div>
</header>

<div class="abs logo-box">
  <span class="logo-mark"></span>
  <span class="logo-name">BRISA PETALS</span>
</div>

<div class="abs search">
  <div class="search-field">Search...</div>
  <div class="search-btn">
    <svg width="18" height="18" viewBox="0 0 18 18"><circle cx="7" cy="7" r="5" fill="none" stroke="#fff" stroke-width="2.2"/><path d="M11 11l5.5 5.5" stroke="#fff" stroke-width="3" stroke-linecap="round"/></svg>
  </div>
</div>

<nav class="abs mainnav">
  <span class="current" style="width:223px">Home</span>
  <span style="width:103px">About Us</span>
  <span style="width:81px">Shop</span>
  <span style="width:106px">Curated</span>
  <span style="width:251px;border-right:none;justify-content:flex-start;padding-left:27px">Contact Us</span>
</nav>

<div class="abs hero" role="img" aria-label="Slideshow photo of white daisies"></div>
<div class="abs hero-arrow" style="left:92px"><svg width="9" height="13" viewBox="0 0 9 13"><path d="M7 1L2 6.5 7 12" fill="none" stroke="#fff" stroke-width="2.2"/></svg></div>
<div class="abs hero-arrow" style="left:569px"><svg width="9" height="13" viewBox="0 0 9 13"><path d="M2 1l5 5.5L2 12" fill="none" stroke="#fff" stroke-width="2.2"/></svg></div>

<aside class="abs promo-wedding" role="img" aria-label="Wedding bouquet promotion with pink roses and lavender">
  <span class="label">Wedding</span><span class="sub">bouquets</span>
  <span class="off">-15</span><span class="more">Read More</span>
</aside>

<aside class="abs promo-shipping">
  <svg class="abs" style="left:14px;top:32px" width="46" height="46" viewBox="0 0 46 46"><path d="M23 8L40 16 23 24 6 16z M6 16v16l17 8 17-8V16 M23 24v16" fill="none" stroke="#fff" stroke-width="3.2" stroke-linejoin="round"/></svg>
  <span class="title">Free Shipping</span>
  <span class="sub">on order over $99</span>
</aside>

<div class="abs section-head curated-head">Curated Collections<span class="all">View all collections →</span></div>

<article class="abs card" style="left:92px;top:546px"><div class="photo" role="img" aria-label="Pink and white lilies" style="background:linear-gradient(135deg,#3f5a35,#e7c3d2 50%,#2e4a2d)"></div><p class="name">California Lillies</p><div class="price-row"><span class="price">$50.00</span><span class="was">$ 75.00</span></div><span class="add">ADD TO CART</span></article>
<article class="abs card" style="left:274px;top:546px"><div class="photo" role="img" aria-label="Bunch of red roses" style="background:linear-gradient(135deg,#8e1420,#c4232f 50%,#6d0f18)"></div><p class="name">Ruby Roses</p><div class="price-row"><span class="price">$40.00</span><span class="was">$ 75.00</span></div><span class="add">ADD TO CART</span></article>
<article class="abs card" style="left:455px;top:546px"><div class="photo" role="img" aria-label="Pink gerbera bouquet in kraft paper" style="background:linear-gradient(135deg,#9aa070,#e9628a 45%,#c9a77a)"></div><p class="name">Spring time</p><div class="price-row"><span class="price">$50.00</span><span class="was">$ 75.00</span></div><span class="add">ADD TO CART</span></article>
<article class="abs card" style="left:92px;top:779px"><div class="photo" role="img" aria-label="Orange and yellow lilies" style="background:linear-gradient(135deg,#f08a2e,#f4d23c 50%,#5b7a3a)"></div><p class="name">Spring time</p><div class="price-row"><span class="price">$50.00</span><span class="was">$ 75.00</span></div><span class="add">ADD TO CART</span></article>
<article class="abs card" style="left:274px;top:779px"><div class="photo" role="img" aria-label="White calla lilies on wood" style="background:linear-gradient(135deg,#5d5d58,#f1f1ea 50%,#4f7a35)"></div><p class="name">California Lillies</p><div class="price-row"><span class="price">$50.00</span><span class="was">$ 75.00</span></div><span class="add">ADD TO CART</span></article>
<article class="abs card" style="left:455px;top:779px"><div class="photo" role="img" aria-label="Pink stargazer lilies" style="background:linear-gradient(135deg,#2f5a33,#e58fb4 50%,#3c6b3a)"></div><p class="name">Ruby Roses</p><div class="price-row"><span class="price">$40.00</span><span class="was">$ 75.00</span></div><span class="add">ADD TO CART</span></article>

<div class="abs section-head fresh-head">Fresh this week</div>
<section class="abs fresh-panel">
  <div class="fresh-item" style="top:20px"><div class="thumb" role="img" aria-label="Orange and yellow lilies" style="background:linear-gradient(135deg,#f08a2e,#f4d23c 50%,#5b7a3a)"></div><span class="name">California Lillies</span><div class="prices"><span class="now">$50.00</span><span class="old">$75.00</span></div><span class="buy">Buy Now</span></div>
  <div class="fresh-item" style="top:111px"><div class="thumb" role="img" aria-label="Pink gerbera bouquet" style="background:linear-gradient(135deg,#9aa070,#e9628a 45%,#c9a77a)"></div><span class="name">California Lillies</span><div class="prices"><span class="now">$40.00</span><span class="old">$75.00</span></div><span class="buy">Buy Now</span></div>
  <div class="fresh-item" style="top:197px"><div class="thumb" role="img" aria-label="White calla lilies" style="background:linear-gradient(135deg,#5d5d58,#f1f1ea 50%,#4f7a35)"></div><span class="name">California Lillies</span><div class="prices"><span class="now">$30.00</span><span class="old">$75.00</span></div><span class="buy">Buy Now</span></div>
  <div class="fresh-item" style="top:284px;border-bottom:none"><div class="thumb" role="img" aria-label="Pink stargazer lilies" style="background:linear-gradient(135deg,#2f5a33,#e58fb4 50%,#3c6b3a)"></div><span class="name">California Lillies</span><div class="prices"><span class="now">$50.00</span><span class="old">$75.00</span></div><span class="buy">Buy Now</span></div>
</section>

<footer class="abs footer">
  <div class="abs" style="left:92px;top:15px">
    <h3>Quick Link</h3>
    <ul><li>Home</li><li>About Us</li><li>Shop</li><li>Curated</li><li>Contact Us</li></ul>
  </div>
  <div class="abs" style="left:222px;top:15px;width:185px">
    <h3>Meet Brisa</h3>
    <p>Based in Hillcrest, San Diego - We offer farm fresh, curated, cool, and same day delivery flower bouquets.</p>
    <div class="social"><span></span><span></span><span></span></div>
  </div>
  <div class="abs" style="left:452px;top:15px">
    <h3>Reach Brisa</h3>
    <p>2210 Marigold Lane<br>San Diego, CA 92100</p>
    <p class="dark" style="margin-top:8px">Email: info@brisapetals.example<br>Phone: 555-014-2290</p>
  </div>
  <div class="abs" style="left:642px;top:15px;width:214px">
    <h3>Newsletter</h3>
    <p style="width:190px">We promise to only send you good things like discounts!</p>
    <div class="newsletter"><div class="field">Email Id</div><div class="btn">Sign Up</div></div>
  </div>
</footer>

<div class="abs copyright">Copyright © 2014 brisapetals of San Diego. Website builder by Quillcart.</div>

</body>
</html>
```